Flyer for family counseling

For my family counseling I'm looking for a design for flyers. Important is not only the appearance of the flyer, but also the content design. All important contents can be found on my website: www.helga-brandtner.at The following items should NOT appear on the flyer: - constellation work - bereavement and palliative work My logo should definitely be on the flyer. Source files are available.

Target Market(s)

Families, individuals, children, couples in need of psychological support.

Colors

Designer to choose colors to be used in the design.

Requirements
Must have
• My logo - source files available Website and contact data Recognition value from website to flyer and vice versa
Should not have
• Mention of the constellation work and mourning and palliative work not desired.

```html
<!DOCTYPE html>
<html lang="de">
<head>
<meta charset="utf-8">
<title>Familienberatung – Flyer</title>
<link href="https://fonts.googleapis.com/css2?family=Fira+Sans:ital,wght@0,400;0,500;0,600;1,600&family=Fira+Sans+Condensed:wght@600;700&display=swap" rel="stylesheet">
<style>
  :root{
    --white:#ffffff;
    --grey-title:#4b4b4d;
    --text:#3b3b3b;
    --blue:#1b6fb8;
    --blue-band:#1474c0;
    --teal:#1fa89d;
    --teal-box:#22a99c;
    --tab:#4f5053;
    --bullet-teal:#20a394;
  }
  *{margin:0;padding:0;box-sizing:border-box}
  html,body{width:988px;height:1200px;overflow:hidden;background:var(--white)}
  body{font-family:"Fira Sans",sans-serif;color:var(--text);position:relative}
  .abs{position:absolute}

  .brand{left:40px;top:168px;width:460px;display:flex;align-items:center;justify-content:center;gap:14px}
  .brand-dot{width:34px;height:34px;border-radius:50%;background:var(--teal)}
  .brand-name{font-family:"Fira Sans",sans-serif;font-weight:500;font-size:28px;letter-spacing:1px;color:var(--blue)}

  .title{right:58px;top:55px;text-align:right;font-family:"Fira Sans Condensed",sans-serif;font-weight:700;font-size:92px;line-height:80px;color:var(--grey-title);letter-spacing:1px}
  .tagline{right:58px;top:226px;text-align:right;font-style:italic;font-weight:600;font-size:32px;line-height:40px;color:var(--teal)}

  .services{left:50px;top:270px;list-style:none}
  .services li{display:flex;align-items:center;height:52.5px;font-family:"Fira Sans Condensed",sans-serif;font-weight:700;font-size:35px;color:var(--blue)}
  .services .dot{width:32px;height:32px;border-radius:50%;background:var(--bullet-teal);border:3px solid #d6d6d6;box-shadow:0 2px 3px rgba(0,0,0,.3);margin-right:25px}

  .intro{left:49px;top:502px;width:432px;font-size:14.5px;line-height:18.4px}
  .divider{left:495px;top:485px;width:2px;height:175px;background:linear-gradient(#fff,#cfcfcf,#fff)}

  .person{right:57px;top:430px;font-family:"Fira Sans",sans-serif;font-weight:600;font-size:26px;letter-spacing:.5px;color:var(--blue)}
  .creds{right:50px;top:474px;list-style:none;text-align:right;font-size:16px;line-height:21px}
  .creds li{position:relative;padding-right:26px;margin-bottom:6px}
  .creds li::after{content:"";position:absolute;right:0;top:4px;width:13px;height:13px;border-radius:50%;background:radial-gradient(circle at 35% 35%,#5fa8e8,var(--blue) 70%)}

  .band{left:0;top:698px;width:988px;height:502px;background:var(--blue-band)}
  .tab{left:18px;top:647px}
  .tab-url{left:84px;top:660px;font-family:"Fira Sans Condensed",sans-serif;font-weight:600;font-size:35px;color:var(--white)}

  .story{left:49px;top:735px;width:375px;font-size:14px;line-height:18.8px;color:var(--white)}
  .story p{margin-bottom:12px}

  .contact{left:40px;top:1022px;width:385px;height:149px;border:3px solid var(--white);border-radius:10px;background:linear-gradient(#6a6b6e,#4a4b4e);box-shadow:0 3px 6px rgba(0,0,0,.4);color:var(--white);font-family:"Fira Sans Condensed",sans-serif;font-weight:600}
  .contact .row{display:flex;align-items:center;padding-left:20px;border-bottom:1px solid rgba(255,255,255,.7)}
  .contact .row:last-child{border-bottom:none}
  .contact svg{margin-right:14px;flex:none}
  .row.phone{height:60px;font-size:36px}
  .row.web{height:48px;font-size:25px}
  .row.addr{height:38px;font-size:16px}

  .questions{left:548px;top:738px;display:grid;grid-template-columns:174px auto;row-gap:10px;color:var(--white);font-size:14px;letter-spacing:.3px}
  .questions span{display:flex;align-items:center}
  .questions span::before{content:"";width:15px;height:15px;border-radius:50%;background:var(--white);margin-right:9px}

  .benefits{left:539px;top:837px;width:394px;height:128px;background:var(--teal-box);border-radius:10px 10px 0 0;padding:12px 24px 0 24px;list-style:none;color:var(--white);font-weight:500;font-size:15.5px;line-height:19px}
  .benefits li{display:flex;align-items:flex-start;padding:4px 0 6px;border-bottom:1px solid rgba(255,255,255,.8)}
  .benefits li:last-child{border-bottom:none}
  .benefits svg{flex:none;margin:2px 10px 0 0}

  .photo{left:539px;top:965px;width:394px;height:152px;background:linear-gradient(135deg,#7a6a58,#c9b6a0 45%,#8a7a6a 70%,#d9d2c4)}

  .mail{right:55px;top:1139px;display:flex;align-items:center;gap:14px;color:var(--white);font-weight:600;font-size:19px}
</style>
</head>
<body>
  <div class="abs brand">
    <span class="brand-dot"></span>
    <span class="brand-name">HELGA BRANDTNER</span>
  </div>

  <h1 class="abs title">FAMILIEN<br>BERATUNG</h1>
  <p class="abs tagline">Ist Ihr Leben an einem<br>Punkt angekommen<br>der Veränderung bedarf?</p>

  <ul class="abs services">
    <li><span class="dot"></span>EINZELBERATUNG</li>
    <li><span class="dot"></span>PAARBERATUNG</li>
    <li><span class="dot"></span>ERZIEHUNGSBERATUNG</li>
    <li><span class="dot"></span>FAMILIE &amp; KINDER</li>
  </ul>

  <p class="abs intro">Das Ziel einer Familientherapie ist, eine positive Beziehungsveränderung zwischen den einzelnen Familienmitgliedern zu erreichen. Respekt, gegenseitiges Verständnis und Einfühlungsvermögen füreinander sind wesentlich für ein funktionierendes Zusammenleben in einer Familie. Diese Werte können in einer Familienberatung wieder in den Mittelpunkt gerückt beziehungsweise verbessert werden.</p>
  <div class="abs divider"></div>

  <h2 class="abs person">HELGA BRANDTNER</h2>
  <ul class="abs creds">
    <li>Psychosoziale Beraterin</li>
    <li>Systemischer Coach, Supervisorin</li>
    <li>Elternberatung nach § 95 Abs. 1a AußStrG (vor<br>einvernehmlicher Scheidung)</li>
    <li>Familien-, Eltern-oder Erziehungsberatung<br>nach § 107 Abs. 3 Z 1 AußStrG</li>
  </ul>

  <div class="abs band"></div>
  <svg class="abs tab" width="552" height="70" viewBox="0 0 552 70">
    <path d="M0 68 Q20 62 40 40 L62 8 Q68 0 80 0 L440 0 Q452 0 460 8 L510 40 Q530 62 552 68 Z" fill="var(--tab)"/>
  </svg>
  <div class="abs tab-url">www.helga-brandtner.at</div>

  <div class="abs story">
    <p>Neue Wege gehen und/oder herausfordernde Lebenssituationen zu meistern sind ein Geschenk und bieten eine Chance, sich als Mensch weiterzuentwickeln, wenn sie als solche erkannt werden.</p>
    <p>Ich begleite Sie durch einfühlende Gespräche, helfe Ihnen Ihr Potential zu entfalten und Ihre Ressourcen sichtbar zu machen. Impulse werden gesetzt um die großartigen Möglichkeiten zu entdecken die das Leben für Sie bereit hält.</p>
    <p>Gemeinsam erarbeiten wir neue Sichtweisen und eröffnen Wege, die Ihnen Kraft und Mut geben.</p>
  </div>

  <div class="abs contact">
    <div class="row phone">
      <svg width="32" height="32" viewBox="0 0 32 32"><circle cx="16" cy="16" r="14" fill="none" stroke="#fff" stroke-width="2"/><path d="M12 8 L15 12 L13 14 Q14 18 18 20 L20 18 L24 21 L22 24 Q14 24 10 13 Z" fill="#fff"/></svg>
      +43 660 418 27 95
    </div>
    <div class="row web">
      <svg width="30" height="30" viewBox="0 0 30 30" fill="none" stroke="#fff" stroke-width="1.8"><circle cx="15" cy="15" r="13"/><ellipse cx="15" cy="15" rx="6" ry="13"/><path d="M2 15H28M4 8H26M4 22H26"/></svg>
      www.helga-brandtner.at
    </div>
    <div class="row addr">
      <svg width="18" height="24" viewBox="0 0 18 24"><path d="M9 0C4 0 0 4 0 9c0 6 9 15 9 15s9-9 9-15C18 4 14 0 9 0z" fill="#fff"/><circle cx="9" cy="9" r="3.5" fill="#5a5b5e"/></svg>
      Donaufelder Gasse 12/3/7, 1220 Wien
    </div>
  </div>

  <div class="abs questions">
    <span>ANGELERNTE ?</span><span>UNANGEBRACHTE ?</span>
    <span>UNANGENEHME ?</span><span>FESTGEFAHRENE ?</span>
    <span>EINGEFAHRENE ?</span>
  </div>

  <ul class="abs benefits">
    <li><svg width="18" height="18" viewBox="0 0 18 18"><circle cx="9" cy="9" r="8" fill="#fff"/><path d="M5 9l3 3 5-6" fill="none" stroke="var(--teal-box)" stroke-width="2.2"/></svg>Menschen in ihrer Entwicklung begleiten</li>
    <li><svg width="18" height="18" viewBox="0 0 18 18"><circle cx="9" cy="9" r="8" fill="#fff"/><path d="M5 9l3 3 5-6" fill="none" stroke="var(--teal-box)" stroke-width="2.2"/></svg>Aufmerksamkeit, Ruhe und Gelassenheit</li>
    <li><svg width="18" height="18" viewBox="0 0 18 18"><circle cx="9" cy="9" r="8" fill="#fff"/><path d="M5 9l3 3 5-6" fill="none" stroke="var(--teal-box)" stroke-width="2.2"/></svg>Klare Strukturen und ein richtig<br>verstandener Zugang zu Disziplin</li>
  </ul>

  <div class="abs photo" role="img" aria-label="Foto: Beraterin im Gespräch mit einer Familie, Eltern und zwei Kinder auf einem Sofa"></div>

  <div class="abs mail">
    <svg width="42" height="30" viewBox="0 0 42 30"><rect x="1" y="1" width="36" height="24" fill="#fff"/><path d="M1 1 L19 15 L37 1" fill="none" stroke="#9cc3e6" stroke-width="2"/><path d="M30 24 H41 M30 24 l5 -4 M30 24 l5 4" stroke="#fff" stroke-width="2.4" fill="none"/></svg>
    familienberatung@helga-brandtner.at
  </div>
</body>
</html>
```